General Contractor Signage for Shopping Mall

Relvan Builders is owned by Tavin Kordell, a licensed general contractor with an additional license in tile. His expertise covers building custom homes from design to finish, remodeling kitchens and bathrooms, doors, windows,prefinished hardwood floors, decking, fences, fireplaces, etc. So many things too numerous to mention. He is looking for an eye catching sign to be set as a kiosk in a major shopping mall and I will upload the specs needed for that. He likes the idea of photos scattered as a background and no too much writing and you can use generic clip art of custom homes, remodeled rooms (kitchen and bathroom), roll of blue prints, scattered tiles, fireplace, fences etc. I will upload the front of his business card although all we want is the name of the company, phone, website and e mail address and license very small. e mail address which is tavinkordell@brightmail.example. We don't need Tavin Kordell on there or the toolbelt. We also want the words "Call for free in home consultation for your home improvement needs" or something to that effect.

Project Deadline Extended
Reason: The designers are not reading our instructions. But we do appreciate their efforts and the designs are very attractive. We do not want unprofessional photos from our website. We don't want the picture of Tavin Kordell. We want the photos scattered as in a collage, not straight. Only one design had this. White border around pictures doesn't have to be that wide. Since it is a big sign, we would like lots of photos of home improvement. Call today for a free in home consultation for all your home improvement needs should be displayed prominently. Thanks.

We would like to thank you for all your submissions. We have added a file of our own pictures that we took ourselves. Please use the ones you like best and create a design of your own.

Target Market(s)

Middle to upper class income adults. Homeowners.

Industry/Entity Type

Home Improvement

Colors

Designer to choose colors to be used in the design.

Requirements
Must have
• The sign must have photos of home improvement work and state Please "Call for free in home consultation for all your home improvement needs." Website, phone number, license #.
Nice to have
• We would like your ideas but the pictures should be professional clip art and not unprofessional pics taken from our website.
Should not have
• Too much wording. We want to show add through pictures.

```html
<!DOCTYPE html>
<html lang="en">
<head>
<meta charset="utf-8">
<title>Relvan Builders – Mall Kiosk Signs</title>
<link href="https://fonts.googleapis.com/css2?family=Oswald:wght@500;700&display=swap" rel="stylesheet">
<style>
  :root{
    --bg:#e9e7e3;
    --ink:#111111;
    --paper:#ffffff;
    --gold:#f6c40c;
    --navy:#1c2b5a;
    --wood:#8a5a34;
    --sky:#4f7fb7;
    --tile:#b9714d;
    --cream:#e6dcc8;
    --slate:#6f7b80;
  }
  *{box-sizing:border-box;margin:0;padding:0}
  html,body{width:1200px;height:1000px;overflow:hidden;background:var(--bg);font-family:"Oswald",sans-serif}
  .sign{position:absolute;top:67px;width:440px;height:866px;background:var(--ink);overflow:hidden;box-shadow:0 6px 20px rgba(0,0,0,.25)}
  .sign--grid{left:90px}
  .sign--collage{left:670px}
  .photo{position:absolute}
  .header{position:absolute;left:0;top:0;width:440px;height:120px;background:var(--paper)}
  .header__band{position:absolute;left:0;top:22px;width:440px;height:80px;background:var(--gold);clip-path:polygon(0 20%,100% 0,100% 75%,0 100%)}
  .brand{position:absolute;left:40px;top:30px;font-weight:700;font-size:42px;line-height:1;color:var(--navy);text-transform:uppercase;letter-spacing:.5px}
  .brand-mark{position:absolute;right:22px;top:22px;width:34px;height:34px;background:var(--navy)}
  .contact{position:absolute;left:115px;top:555px;width:225px;height:128px;background:var(--ink);border:3px solid var(--gold)}
  .contact__lead{background:var(--gold);color:var(--ink);font-weight:700;font-size:11px;line-height:1.2;text-align:center;padding:4px 4px;text-transform:uppercase}
  .contact__phone{color:var(--paper);font-weight:500;font-size:28px;padding:2px 10px 0}
  .contact__line{color:var(--paper);font-weight:500;font-size:11px;padding:1px 10px}
  .contact__web{margin:5px 8px 0;background:var(--paper);color:var(--ink);font-weight:700;font-size:12px;text-align:center}
  .band{position:absolute;left:0;top:355px;width:440px;height:150px;background:var(--ink);z-index:2}
  .band__left{position:absolute;left:6px;top:14px;width:130px;color:var(--paper);font-weight:700;font-size:14px;line-height:1.35;text-transform:uppercase}
  .band__phone{position:absolute;left:6px;top:96px;color:var(--gold);font-weight:700;font-size:21px}
  .band__right{position:absolute;right:6px;top:14px;width:130px;color:var(--paper);font-weight:700;font-size:14px;line-height:1.35;text-align:right;text-transform:uppercase}
  .band__mail{position:absolute;right:6px;top:88px;color:var(--gold);font-weight:500;font-size:9.5px;text-align:right;line-height:1.5}
  .band__brand{position:absolute;left:150px;top:40px;width:140px;text-align:center;color:var(--gold);font-weight:700;font-size:24px;line-height:1.05;text-transform:uppercase}
  .band__mark{position:absolute;left:212px;top:20px;width:16px;height:16px;background:var(--gold)}
  .band__lic{position:absolute;left:150px;top:100px;width:140px;text-align:center;color:var(--paper);font-size:10px;font-weight:500}
  .scatter{border:3px solid var(--paper)}
</style>
</head>
<body>

<section class="sign sign--grid" aria-label="Kiosk sign, grid layout">
  <div class="header">
    <div class="header__band"></div>
    <div class="brand">Relvan Builders</div>
    <div class="brand-mark"></div>
  </div>
  <div class="photo" role="img" aria-label="Paint brushes and colour swatches" style="left:0;top:120px;width:85px;height:130px;background:linear-gradient(135deg,#c9a46a,#7aa0c8,#d44)"></div>
  <div class="photo" role="img" aria-label="Hand holding a trowel" style="left:88px;top:120px;width:40px;height:130px;background:linear-gradient(160deg,#d9b48f,#8a6a4c)"></div>
  <div class="photo" role="img" aria-label="Open paint cans" style="left:131px;top:120px;width:145px;height:130px;background:radial-gradient(circle at 40% 40%,#e07a2c,#6a8fb0 55%,#cfcac0)"></div>
  <div class="photo" role="img" aria-label="Hand sketching plans" style="left:279px;top:120px;width:161px;height:130px;background:linear-gradient(135deg,#efe7da,#bba58a)"></div>

  <div class="photo" role="img" aria-label="House framing under a blue sky" style="left:0;top:255px;width:180px;height:145px;background:linear-gradient(180deg,var(--sky),#9a7650)"></div>
  <div class="photo" role="img" aria-label="Plywood wall framing" style="left:185px;top:255px;width:75px;height:145px;background:linear-gradient(180deg,#d8c09a,#b0905e)"></div>
  <div class="photo" role="img" aria-label="Room with new drywall and window" style="left:265px;top:255px;width:175px;height:145px;background:linear-gradient(180deg,#e0b78c,#c7a27d)"></div>

  <div class="photo" role="img" aria-label="Light switch on a wall" style="left:0;top:405px;width:65px;height:145px;background:linear-gradient(180deg,#5a5c58,#2f312e)"></div>
  <div class="photo" role="img" aria-label="Scattered floor tiles" style="left:70px;top:405px;width:145px;height:145px;background:linear-gradient(135deg,var(--cream),var(--tile))"></div>
  <div class="photo" role="img" aria-label="Tile samples and blueprints" style="left:220px;top:405px;width:145px;height:145px;background:linear-gradient(135deg,#3e4fa0,#d7d4cc)"></div>
  <div class="photo" role="img" aria-label="Bathroom counter" style="left:370px;top:405px;width:70px;height:145px;background:linear-gradient(180deg,#a9b6bc,#6c7478)"></div>

  <div class="photo" role="img" aria-label="Tiled shower with mosaic panel" style="left:0;top:555px;width:110px;height:311px;background:linear-gradient(180deg,#3f7a78,#2b5054)"></div>
  <div class="contact">
    <div class="contact__lead">Please call for free in home consultation for all your home improvement needs.</div>
    <div class="contact__phone">P: 555.208.4417</div>
    <div class="contact__line">E: tavinkordell@brightmail.example</div>
    <div class="contact__web">www.relvanbuilders.example</div>
  </div>
  <div class="photo" role="img" aria-label="Remodeled white kitchen" style="left:115px;top:688px;width:225px;height:178px;background:linear-gradient(180deg,#f1efe9,#b9b4a8)"></div>
  <div class="photo" role="img" aria-label="Slate tile floor" style="left:345px;top:555px;width:95px;height:311px;background:linear-gradient(135deg,#a88a6a,#6f7b80,#c59a6a)"></div>
</section>

<section class="sign sign--collage" aria-label="Kiosk sign, collage layout">
  <div class="photo scatter" role="img" aria-label="Colour swatches and brushes" style="left:-20px;top:-10px;width:200px;height:150px;transform:rotate(-8deg);background:linear-gradient(135deg,#d44,#f6c40c,#7aa0c8)"></div>
  <div class="photo scatter" role="img" aria-label="Hand with tape measure" style="left:150px;top:-20px;width:170px;height:120px;transform:rotate(6deg);background:linear-gradient(160deg,#d9b48f,#8a6a4c)"></div>
  <div class="photo scatter" role="img" aria-label="Sketching plans on paper" style="left:290px;top:-15px;width:180px;height:140px;transform:rotate(-5deg);background:linear-gradient(135deg,#efe7da,#bba58a)"></div>
  <div class="photo scatter" role="img" aria-label="Open paint cans" style="left:20px;top:110px;width:170px;height:140px;transform:rotate(10deg);background:radial-gradient(circle at 40% 40%,#e07a2c,#6a8fb0 55%,#cfcac0)"></div>
  <div class="photo scatter" role="img" aria-label="Paint colour chart" style="left:170px;top:90px;width:140px;height:160px;transform:rotate(-14deg);background:linear-gradient(90deg,#f39,#6cf,#9c6,#fc3)"></div>
  <div class="photo scatter" role="img" aria-label="Open blueprint book" style="left:290px;top:120px;width:170px;height:160px;transform:rotate(-18deg);background:linear-gradient(135deg,#f4f4f0,#a9b0b8)"></div>
  <div class="photo scatter" role="img" aria-label="Wall framing with insulation" style="left:-15px;top:240px;width:220px;height:140px;transform:rotate(-4deg);background:linear-gradient(180deg,#e0b78c,#b0905e)"></div>
  <div class="photo scatter" role="img" aria-label="House framing" style="left:200px;top:250px;width:250px;height:130px;transform:rotate(3deg);background:linear-gradient(180deg,var(--sky),#9a7650)"></div>

  <div class="band">
    <div class="band__left">Please call for free in home consultation.</div>
    <div class="band__phone">P: 555.208.4417</div>
    <div class="band__mark"></div>
    <div class="band__brand">Relvan Builders</div>
    <div class="band__lic">Lic.# C-00-481726</div>
    <div class="band__right">For all your home improvement needs.</div>
    <div class="band__mail">E: tavinkordell@brightmail.example<br>www.relvanbuilders.example</div>
  </div>

  <div class="photo scatter" role="img" aria-label="Scattered terracotta tiles" style="left:-20px;top:495px;width:210px;height:170px;transform:rotate(-6deg);background:linear-gradient(135deg,var(--cream),var(--tile))"></div>
  <div class="photo scatter" role="img" aria-label="Glass shower enclosure" style="left:170px;top:500px;width:200px;height:160px;transform:rotate(5deg);background:linear-gradient(180deg,#6e9a9c,#3c5f62)"></div>
  <div class="photo scatter" role="img" aria-label="Bathroom vanity" style="left:330px;top:510px;width:140px;height:140px;transform:rotate(-8deg);background:linear-gradient(180deg,#d8d2c4,#8d8779)"></div>
  <div class="photo scatter" role="img" aria-label="Stone countertop" style="left:60px;top:630px;width:190px;height:110px;transform:rotate(9deg);background:linear-gradient(135deg,#c9bfae,#7d6e5c)"></div>
  <div class="photo scatter" role="img" aria-label="Wood-panelled exterior" style="left:260px;top:625px;width:200px;height:110px;transform:rotate(-4deg);background:linear-gradient(180deg,#6f8b5a,var(--wood))"></div>
  <div class="photo scatter" role="img" aria-label="White kitchen with range" style="left:-10px;top:720px;width:150px;height:160px;transform:rotate(-3deg);background:linear-gradient(180deg,#f1efe9,#b9b4a8)"></div>
  <div class="photo scatter" role="img" aria-label="Cherry wood kitchen with steel fridge" style="left:120px;top:710px;width:340px;height:170px;transform:rotate(2deg);background:linear-gradient(90deg,#7a3a1e,#b9b9b9,#8a4a26)"></div>
</section>

</body>
</html>
```